Steady Harbor Claims Group Business card

Need a business card that stands out that includes name of company,(above) Owners name Moira Lindqvist phone#517-362-4408 email# SteadyHarborCG@mailvane.com and website www.Steadyharborclaimsgroup.net. This is a medical billing company so the card has to relate to that or relate to increasing revenue

```html
<!DOCTYPE html>
<html lang="en">
<head>
<meta charset="utf-8">
<title>Steady Harbor Claims Group – Business Card</title>
<link rel="stylesheet" href="https://fonts.googleapis.com/css2?family=Cinzel:wght@500;600&family=Open+Sans:wght@400&display=swap">
<style>
  :root {
    --navy: #1f3f8f;
    --green: #6aaa2e;
    --paper: #f1f1ef;
    --ink: #3a3a3a;
    --backdrop: #8c8d8f;
    --card-w: 745px;
    --card-h: 425px;
  }
  * { margin: 0; padding: 0; box-sizing: border-box; }
  html, body {
    width: 1105px;
    height: 1200px;
    overflow: hidden;
    background: var(--backdrop);
  }
  .sheet {
    position: relative;
    width: 1105px;
    height: 1200px;
  }
  .card {
    position: absolute;
    left: 180px;
    width: var(--card-w);
    height: var(--card-h);
    background: var(--paper);
    overflow: hidden;
  }
  .card--front { top: 120px; }
  .card--back { top: 636px; }

  .brand-decoration {
    position: absolute;
    left: 0;
    top: 0;
    width: 470px;
    height: 425px;
    background: linear-gradient(135deg, rgba(31,63,143,0.22) 0%, rgba(106,170,46,0.22) 100%);
    clip-path: polygon(0 0, 58% 0, 100% 35%, 40% 100%, 0 100%);
  }

  .owner {
    position: absolute;
    right: 36px;
    top: 38px;
    text-align: right;
  }
  .owner__name {
    font-family: "Cinzel", serif;
    font-weight: 600;
    font-size: 29px;
    color: var(--navy);
    letter-spacing: 0.5px;
  }
  .owner__role {
    font-family: "Cinzel", serif;
    font-weight: 500;
    font-size: 21px;
    color: var(--green);
    margin-top: 2px;
  }

  .contact {
    position: absolute;
    right: 36px;
    bottom: 38px;
    list-style: none;
    text-align: right;
  }
  .contact__item {
    display: flex;
    justify-content: flex-end;
    align-items: center;
    gap: 14px;
    font-family: "Open Sans", sans-serif;
    font-size: 19px;
    color: var(--ink);
    height: 36px;
  }
  .contact__icon {
    width: 18px;
    height: 18px;
    flex: none;
    fill: var(--navy);
  }

  .wordmark {
    position: absolute;
    left: 0;
    right: 0;
    top: 50%;
    transform: translateY(-50%);
    display: flex;
    flex-direction: column;
    align-items: center;
    gap: 22px;
  }
  .wordmark__square {
    width: 54px;
    height: 54px;
    background: var(--green);
  }
  .wordmark__name {
    font-family: "Cinzel", serif;
    font-weight: 600;
    font-size: 32px;
    color: var(--navy);
    letter-spacing: 0.5px;
  }
</style>
</head>
<body>
<main class="sheet">

  <section class="card card--front" aria-label="Card front">
    <div class="brand-decoration" role="img" aria-label="Large brand symbol decoration in blue and green"></div>

    <header class="owner">
      <p class="owner__name">Moira Lindqvist</p>
      <p class="owner__role">Owners</p>
    </header>

    <ul class="contact">
      <li class="contact__item">
        <span>517-362-4408</span>
        <svg class="contact__icon" viewBox="0 0 24 24" aria-hidden="true"><path d="M6.6 10.8a15.1 15.1 0 0 0 6.6 6.6l2.2-2.2c.3-.3.7-.4 1-.2 1.1.4 2.3.6 3.6.6.6 0 1 .4 1 1V20c0 .6-.4 1-1 1C10.6 21 3 13.4 3 4c0-.6.4-1 1-1h3.5c.6 0 1 .4 1 1 0 1.3.2 2.5.6 3.6.1.3 0 .7-.2 1z"/></svg>
      </li>
      <li class="contact__item">
        <span>SteadyHarborCG@mailvane.com</span>
        <svg class="contact__icon" viewBox="0 0 24 24" aria-hidden="true"><path d="M2 5h20v14H2z" /><path d="M2 5l10 8 10-8" fill="none" stroke="#f1f1ef" stroke-width="1.8"/></svg>
      </li>
      <li class="contact__item">
        <span>www.Steadyharborclaimsgroup.net</span>
        <svg class="contact__icon" viewBox="0 0 24 24" aria-hidden="true"><circle cx="12" cy="12" r="10"/><path d="M2 12h20M12 2c3 3 3 17 0 20M12 2c-3 3-3 17 0 20" fill="none" stroke="#f1f1ef" stroke-width="1.4"/></svg>
      </li>
    </ul>
  </section>

  <section class="card card--back" aria-label="Card back">
    <div class="wordmark">
      <span class="wordmark__square" aria-hidden="true"></span>
      <p class="wordmark__name">Steady Harbor Claims Group</p>
    </div>
  </section>

</main>
</body>
</html>
```